Sample Box for Collegiate Alumni Fundraising

We are a screen printing and embroidery company. Our core services are 1) printing & embroidery on apparel (t-shirts, hoodies etc) 2) promo products like mugs, stickers and 3) fulfillment (shipping orders to individuals that have placed orders.
I would like a sample box designed for our specific target market - College and university alumni giving offices. These offices are in charge of running fundraising campaigns. The two main types of campaigns are Giving Day (each school choses their own unique date but most are in the spring) and Open Hand Week (this is a set date each year which occurs the Tuesday after Thanksgiving). Many schools host their own day as well as participate in Open Hand Week. Oftentimes we are tasked with research and tracking down the right product for each campaign.
I have attached two examples that we had created for running clubs. I am open to both real photos or illustrations. I do not want to match these examples, I just want to demonstrate the general design of a sample box.
I do want to highlight our services on side panels like the examples. Printing, Fulfillment, Product Options

```html
<!DOCTYPE html>
<html lang="en">
<head>
<meta charset="utf-8">
<title>Giving Day Sample Box – Dielines</title>
<link href="https://fonts.googleapis.com/css2?family=Marcellus&family=Marcellus+SC&family=Poppins:wght@400;500;600&family=Great+Vibes&display=swap" rel="stylesheet">
<style>
  :root{
    --stage:#bfbfbf;
    --stage-light:#cfcfcf;
    --deep-blue:#0a7fc4;
    --mid-blue:#1391d2;
    --dark-blue:#0671b3;
    --sky:#74c9e6;
    --sky-core:#5dbedc;
    --sky-pale:#93d2ea;
    --white:#ffffff;
    --orange:#f08a24;
    --line:#cfe9f7;
  }
  html,body{margin:0;padding:0;width:1200px;height:957px;overflow:hidden;background:var(--stage);}
  .board{display:block;width:1200px;height:957px;}
  .serif-display{font-family:"Marcellus",serif;}
  .serif-caps{font-family:"Marcellus SC","Marcellus",serif;}
  .sans{font-family:"Poppins",sans-serif;}
  .script{font-family:"Great Vibes",cursive;}
</style>
</head>
<body>
<svg class="board" viewBox="0 0 1500 1196" width="1200" height="957" xmlns="http://www.w3.org/2000/svg">
  <defs>
    <radialGradient id="stage-glow" cx="50%" cy="45%" r="70%">
      <stop offset="0" stop-color="var(--stage-light)"/>
      <stop offset="1" stop-color="var(--stage)"/>
    </radialGradient>
    <linearGradient id="outer-blue" gradientUnits="userSpaceOnUse" x1="120" y1="120" x2="700" y2="1030">
      <stop offset="0" stop-color="#1b8fd3"/>
      <stop offset="0.35" stop-color="var(--deep-blue)"/>
      <stop offset="0.7" stop-color="var(--mid-blue)"/>
      <stop offset="1" stop-color="var(--dark-blue)"/>
    </linearGradient>
    <linearGradient id="inner-sky" gradientUnits="userSpaceOnUse" x1="800" y1="120" x2="1370" y2="1035">
      <stop offset="0" stop-color="#7fcbe6"/>
      <stop offset="1" stop-color="var(--sky-pale)"/>
    </linearGradient>
    <filter id="lift" x="-10%" y="-10%" width="120%" height="120%">
      <feDropShadow dx="6" dy="8" stdDeviation="8" flood-color="#000" flood-opacity="0.28"/>
    </filter>
  </defs>

  <rect class="stage" width="1500" height="1196" fill="url(#stage-glow)"/>

  <!-- ============ OUTSIDE DIELINE ============ -->
  <g class="dieline dieline--outside">
    <g class="dieline-shape" fill="url(#outer-blue)" filter="url(#lift)">
      <rect x="238" y="119" width="349" height="530"/>
      <rect x="121" y="237" width="584" height="285"/>
      <rect x="130" y="645" width="567" height="270" rx="48"/>
      <rect x="238" y="900" width="349" height="30"/>
      <path d="M140,922 H687 Q697,922 697,935 V945 Q697,1033 605,1033 H222 Q130,1033 130,945 V935 Q130,922 140,922 Z"/>
    </g>

    <g class="bubbles" fill="#ffffff" fill-opacity="0.06">
      <circle cx="330" cy="370" r="105"/>
      <circle cx="520" cy="420" r="80"/>
      <circle cx="180" cy="480" r="75"/>
      <circle cx="470" cy="780" r="95"/>
      <circle cx="260" cy="760" r="60"/>
    </g>

    <!-- Lid panel, printed upside down -->
    <g class="lid-panel" transform="rotate(180 413 380)">
      <text class="serif-display" x="413" y="386" text-anchor="middle" font-size="50" fill="var(--white)" letter-spacing="1">GIVING DAY</text>
      <text class="serif-display" x="413" y="418" text-anchor="middle" font-size="28" fill="var(--orange)">Campaign</text>
      <rect x="288" y="427" width="250" height="21" rx="10.5" fill="none" stroke="var(--white)" stroke-width="1.2"/>
      <text class="sans" x="413" y="442" text-anchor="middle" font-size="12.5" fill="var(--white)">Solutions for Alumni Engagement</text>
      <text class="sans" x="413" y="462" text-anchor="middle" font-size="6.5" font-weight="600" fill="var(--white)" letter-spacing="0.3">CUSTOM APPAREL • PROMOTIONAL PRODUCTS • FULFILLMENT</text>
    </g>
    <g role="img" aria-label="Small orange butterfly illustration">
      <ellipse cx="296" cy="432" rx="8" ry="10" fill="var(--orange)"/>
    </g>
    <g role="img" aria-label="Line-art butterfly ornament">
      <ellipse cx="175" cy="472" rx="52" ry="40" fill="#ffffff" fill-opacity="0.08"/>
    </g>
    <g role="img" aria-label="Line-art butterfly ornament">
      <ellipse cx="570" cy="265" rx="50" ry="35" fill="#c8a26a" fill-opacity="0.15"/>
    </g>

    <!-- Product options panel -->
    <g role="img" aria-label="Large translucent butterfly illustration">
      <ellipse cx="430" cy="770" rx="105" ry="118" fill="#5a8fb0" fill-opacity="0.28"/>
    </g>
    <g role="img" aria-label="Small orange butterfly illustration">
      <ellipse cx="511" cy="706" rx="7" ry="9" fill="var(--orange)"/>
    </g>
    <g class="product-options">
      <text class="serif-caps" x="413" y="734" text-anchor="middle" font-size="19" fill="var(--white)" letter-spacing="1">PRODUCT OPTIONS</text>
      <line x1="303" y1="739" x2="523" y2="739" stroke="var(--white)" stroke-width="1.2"/>

      <g class="icon icon-mug" fill="none" stroke="var(--white)" stroke-width="1.4">
        <rect x="344" y="758" width="14" height="18" rx="2"/>
        <path d="M358,762 h4 a3 3 0 0 1 0 9 h-4"/>
      </g>
      <g class="icon icon-sticker" fill="none" stroke="var(--white)" stroke-width="1.4">
        <circle cx="399" cy="764" r="6"/>
        <path d="M396,766 q3,3 6,0"/>
        <path d="M408,778 v-8 h4 l3,-5 v5 h4 v8 z"/>
        <path d="M417,760 l3,3 l3,-3 a2 2 0 0 0 -6,0"/>
      </g>
      <g class="icon icon-apparel" fill="none" stroke="var(--white)" stroke-width="1.4">
        <path d="M467,758 l-7,5 v16 h26 v-16 l-7,-5 q-6,5 -12,0 z"/>
        <line x1="473" y1="763" x2="473" y2="779"/>
      </g>
      <text class="sans" font-size="11" fill="var(--white)" text-anchor="middle">
        <tspan x="353" y="797">Mugs</tspan>
        <tspan x="409" y="797">Stickers</tspan>
        <tspan x="473" y="797">Apparel</tspan>
      </text>
      <text class="sans" font-size="10" fill="var(--white)" text-anchor="middle" opacity="0.8"><tspan x="377" y="797">|</tspan><tspan x="441" y="797">|</tspan></text>
      <line x1="335" y1="810" x2="495" y2="810" stroke="var(--white)" stroke-width="0.8" opacity="0.7"/>

      <g class="icon icon-gift" fill="none" stroke="var(--white)" stroke-width="1.4">
        <rect x="361" y="830" width="17" height="14"/>
        <rect x="359" y="825" width="21" height="5"/>
        <line x1="369.5" y1="825" x2="369.5" y2="844"/>
        <path d="M369.5,825 q-7,-7 -7,-2 q0,2 7,2 q7,-7 7,-2 q0,2 -7,2"/>
      </g>
      <g class="icon icon-merch" fill="none" stroke="var(--white)" stroke-width="1.4">
        <circle cx="437" cy="832" r="7"/>
        <path d="M446,826 l8,-4 v14 l-8,-4 z"/>
        <circle cx="451" cy="844" r="3"/>
      </g>
      <text class="sans" font-size="11" fill="var(--white)" text-anchor="middle">
        <tspan x="369" y="861">Gifts</tspan>
        <tspan x="441" y="861">Campaign</tspan>
        <tspan x="441" y="872">Merchandise</tspan>
      </text>
      <text class="sans" font-size="10" fill="var(--white)" text-anchor="middle" opacity="0.8" x="393" y="861">|</text>
    </g>

    <!-- Side panel: fulfillment -->
    <g class="side-panel side-fulfillment" transform="translate(190 732) rotate(90)">
      <rect x="-48" y="-11" width="96" height="22" rx="11" fill="none" stroke="var(--white)" stroke-width="1.2"/>
      <text class="serif-display" x="0" y="6" text-anchor="middle" font-size="17" fill="var(--white)">Fulfillment</text>
    </g>
    <g class="side-panel side-fulfillment-copy" transform="translate(172 690) rotate(90)">
      <text class="sans" font-size="8.5" font-weight="500" fill="var(--white)">
        <tspan x="0" y="0">From packaging to individual delivery,</tspan>
        <tspan x="0" y="11">we handle every order.</tspan>
      </text>
    </g>

    <!-- Side panel: printing -->
    <g class="side-panel side-printing" transform="translate(626 800) rotate(-90)">
      <rect x="-50" y="-11" width="100" height="22" rx="11" fill="none" stroke="var(--white)" stroke-width="1.2"/>
      <text class="serif-display" x="0" y="6" text-anchor="middle" font-size="17" fill="var(--white)">Printing</text>
    </g>
    <g class="side-panel side-printing-copy" transform="translate(652 848) rotate(-90)">
      <text class="sans" font-size="8.5" font-weight="500" fill="var(--white)">
        <tspan x="0" y="0">Custom t-shirts, hoodies, apparel and</tspan>
        <tspan x="0" y="11">campaign merchandise designed to</tspan>
        <tspan x="0" y="22">engage supporters</tspan>
      </text>
    </g>

    <!-- Front tuck -->
    <g class="front-tuck">
      <rect x="310" y="955" width="213" height="21" rx="10.5" fill="none" stroke="var(--white)" stroke-width="1.2"/>
      <text class="serif-display" x="416" y="970" text-anchor="middle" font-size="14" fill="var(--white)">Helping alumni campaigns</text>
      <text x="413" y="998" text-anchor="middle" fill="var(--white)"><tspan class="script" font-size="23">Create</tspan><tspan class="sans" font-size="11.5" dx="3">Meaningful Connections</tspan></text>
    </g>
  </g>

  <!-- ============ INSIDE DIELINE ============ -->
  <g class="dieline dieline--inside">
    <g class="dieline-shape" fill="url(#inner-sky)" filter="url(#lift)">
      <path d="M803,232 V200 Q803,122 880,122 H1290 Q1368,122 1368,200 V232 Z"/>
      <rect x="803" y="240" width="565" height="276" rx="50"/>
      <rect x="795" y="632" width="580" height="286"/>
      <rect x="912" y="122" width="345" height="913"/>
    </g>
    <rect class="center-band" x="912" y="122" width="345" height="913" fill="var(--sky-core)" opacity="0.55"/>

    <g class="bubbles" fill="#ffffff" fill-opacity="0.08">
      <circle cx="875" cy="355" r="45"/>
      <circle cx="1010" cy="320" r="85"/>
      <circle cx="1200" cy="380" r="35"/>
      <circle cx="1340" cy="440" r="60"/>
      <circle cx="1150" cy="760" r="120"/>
      <circle cx="1010" cy="720" r="65"/>
    </g>

    <g role="img" aria-label="Large translucent butterfly illustration">
      <ellipse cx="1080" cy="375" rx="100" ry="115" fill="#4e9fae" fill-opacity="0.35"/>
    </g>
    <g role="img" aria-label="Line-art butterfly ornament">
      <ellipse cx="1320" cy="680" rx="50" ry="38" fill="#ffffff" fill-opacity="0.12"/>
    </g>
    <g role="img" aria-label="Line-art butterfly ornament">
      <ellipse cx="920" cy="885" rx="48" ry="32" fill="#c8a26a" fill-opacity="0.2"/>
    </g>
    <g role="img" aria-label="Small orange butterfly illustration">
      <ellipse cx="1203" cy="723" rx="7" ry="9" fill="var(--orange)"/>
    </g>

    <text class="serif-display" x="1083" y="778" text-anchor="middle" font-size="52" fill="var(--white)" letter-spacing="1">GIVING DAY</text>
  </g>
</svg>
</body>
</html>
```